Professional stationery for boutique management consulting business

I need branded business stationery for my consulting business, using our existing logo and website branding. We consult to senior executives to create deep cultural change needed for humane, people-centred workplaces. The key deliverables are: (A4 size) business letterheads, proposal cover, project folder, report template, email footer, business card, simple powerpoint template. A warm, empowering and expert tone of voice is important as it needs to bridge the gap between academia and industry. It should be clean and professional without feeling "over-branded".
I would like to see stationery designs that use my website colours and design elements (see attached file), especially the delta logo. Our fonts are Operetta and Sofia Pro.
Updates

Thanks for the designs sent so far. Just to confirm that our key deliverables for this project are: - (A4 size) business letterhead - (A4 size) proposal template - (A4 size) report template - Project folder, - Simple powerpoint template - Business card Many thanks

Target Market(s)

Senior executives and business professionals with an interest in business school thinking.

Industry/Entity Type

Management consulting and executive coaching

Font styles to use
Other font styles liked:
• Operetta and Sofia Pro

Colors
0054AA
0677BA
7BADD7
CADEEF
E8F1F8

Requirements
Must have
• Clean professional design that ties in closely to complement and extend the design elements in my website: marlowadvises.com
Nice to have
• Address and contact details I can edit in Microsoft Word, Outlook for Mac, etc
Should not have
• Excessive brand elements, fussy design and additional colours.

```html
<!DOCTYPE html>
<html lang="en">
<head>
<meta charset="utf-8">
<title>Marlow Advisory – Stationery Suite</title>
<link href="https://fonts.googleapis.com/css2?family=Playfair+Display:wght@400;700&family=Jost:wght@300;400;500;600&display=swap" rel="stylesheet">
<style>
:root{
  --brand:#0054AA;
  --brand-mid:#0677BA;
  --brand-soft:#7BADD7;
  --brand-pale:#CADEEF;
  --brand-mist:#E8F1F8;
  --ink:#2b2f36;
  --grey-bg:#a7a9ad;
  --paper:#ffffff;
  --serif:'Playfair Display', Georgia, serif;
  --sans:'Jost', Arial, sans-serif;
}
*{box-sizing:border-box;margin:0;padding:0}
html,body{width:1200px;height:857px;overflow:hidden}
body{background:var(--grey-bg);position:relative;font-family:var(--sans);color:var(--ink)}
.piece{position:absolute;background:var(--paper);overflow:hidden;box-shadow:0 1px 3px rgba(0,0,0,.18)}
.abs{position:absolute}
.brand{position:absolute;display:flex;align-items:center;gap:3px;font-family:var(--serif);color:var(--brand);line-height:.95}
.brand .mark{width:.7em;height:.7em;background:var(--brand);flex:none}
.brand.on-blue{color:#fff}
.brand.on-blue .mark{background:#fff}
.tiny{font-size:3.2px;line-height:1.45;color:var(--ink)}
.contact{font-size:3px;line-height:1.5;color:var(--ink)}
.contact i{display:inline-block;width:2.4px;height:2.4px;border-radius:50%;background:var(--brand);margin-right:2px;vertical-align:middle}
.ripple{background:radial-gradient(ellipse at 70% 55%, #dfe6ee 0%, #eef2f6 35%, #f4f6f9 70%)}
/* slides */
.slide{width:246px;height:154px;background:#f1f4f7}
.slide-title .headline{left:18px;top:80px;font-family:var(--serif);font-size:13.5px;color:var(--brand)}
.slide-title .tagline{left:18px;top:96px;font-size:6.5px}
.slide-title .byline{left:18px;top:120px;font-size:3.6px;line-height:1.35}
.byline b{color:var(--brand);font-weight:600}
.slide-bio .band{left:0;top:0;width:81px;height:154px;background:var(--brand)}
.slide-bio .portrait{left:24px;top:20px;width:75px;height:114px;background:linear-gradient(180deg,#8fae88 0%,#6d8a74 45%,#2e4a7a 75%,#24406e 100%)}
.slide-bio .copy{left:117px;top:18px;width:114px}
.slide-bio h3{font-family:var(--serif);font-weight:400;font-size:6.3px;color:var(--brand);line-height:1.2}
.slide-bio .role{font-size:3.6px;font-style:italic;color:var(--brand);margin-top:3px}
.rule{width:9px;height:1.2px;background:var(--brand);margin:4px 0 8px}
.slide-bio p{font-size:3px;line-height:1.4;text-align:justify;margin-bottom:4px}
.slide-services .intro{left:0;width:246px;top:30px;text-align:center;font-size:4.6px;line-height:1.4}
.slide-services .dash{left:118px;top:23px;width:11px;height:1.2px;background:var(--brand)}
.service{position:absolute;top:56px;width:64px;height:80px;background:#fff;border:.5px solid #dde3ea;border-radius:3px;text-align:center;padding:44px 4px 0;font-size:3.5px;line-height:1.35}
.service b{font-weight:600}
.service svg{position:absolute;left:19px;top:10px}
.service .corner{position:absolute;left:0;top:0;width:0;height:0;border-top:5px solid var(--brand);border-right:5px solid transparent}
.slide-thanks{background:#f4f5f7}
.slide-thanks .scene{right:0;top:0;width:110px;height:154px;background:linear-gradient(160deg,#eceef1 0%,#fafafa 45%,#dfe2e6 100%)}
.slide-thanks .headline{left:19px;top:64px;font-family:var(--serif);font-size:24px;color:var(--brand)}
.slide-thanks .tagline{left:19px;top:93px;font-size:7.5px}
.slide-thanks .accr{left:200px;top:117px;font-size:3.6px;font-weight:600;color:var(--brand)}
.badge{position:absolute;top:124px;background:var(--brand-soft)}
/* letterhead */
.letterhead{left:644px;top:154px;width:200px;height:284px}
.letterhead .body{left:21px;top:68px;width:158px}
.letterhead .body p{font-size:2.9px;line-height:1.55;margin-bottom:5px;text-align:justify}
.signature{font-family:var(--serif);font-style:italic;font-size:6px;color:#333}
/* cards */
.card{width:94px;height:53px}
.card-back{background:var(--brand)}
.card-back .strap{left:7px;top:42px;color:#fff;font-family:var(--serif);font-size:2.6px;font-weight:700}
.card-back .strap span{display:block;font-family:var(--sans);font-weight:300;font-size:1.9px}
.divider{width:.4px;background:#c9d3de}
/* email */
.email{left:869px;top:290px;width:180px;height:55px}
.email .avatar{left:10px;top:8px;width:32px;height:32px;border-radius:50%;background:linear-gradient(160deg,#9bb49a,#4f6b86)}
.email .rule-bottom{left:0;bottom:0;width:180px;height:2px;background:var(--brand)}
.dot{position:absolute;top:43px;width:4.5px;height:4.5px;border-radius:50%;background:var(--brand)}
/* envelopes */
.envelope{width:219px}
.env-front{left:101px;top:457px;height:96px}
.env-back{left:101px;top:568px;height:97px;background:#fff}
/* proposal */
.proposal{left:343px;top:458px;width:401px;height:284px;background:#fff}
.proposal .back{left:0;top:0;width:200px;height:284px;background:var(--brand)}
.proposal .water{left:200px;top:150px;width:201px;height:134px;background:linear-gradient(180deg,#fff 0%,#e6ebf1 40%,#cdd7e3 100%)}
.proposal .kicker{left:223px;top:117px;font-family:var(--serif);font-size:11.5px;color:var(--ink)}
.proposal .title{left:223px;top:129px;font-family:var(--serif);font-weight:700;font-size:20px;color:var(--brand)}
.proposal .date{left:223px;top:151px;font-size:3.6px}
/* folder */
.folder{left:752px;top:462px;width:380px;height:270px;background:transparent;box-shadow:none}
.folder .inner{left:0;top:0;width:190px;height:270px;background:var(--brand);box-shadow:0 1px 3px rgba(0,0,0,.2)}
.folder .cover{left:190px;top:0;width:190px;height:270px;background:#fff;box-shadow:0 1px 3px rgba(0,0,0,.2)}
.folder .strap{right:10px;top:218px;text-align:right;color:#fff;font-family:var(--serif);font-weight:700;font-size:6px}
.folder .strap span{display:block;font-family:var(--sans);font-weight:300;font-size:4px}
.contact.light{color:#fff}
.contact.light i{background:#fff}
</style>
</head>
<body>

<!-- Presentation: title slide -->
<section class="piece slide slide-title" style="left:101px;top:115px">
  <div class="abs ripple" role="img" aria-label="Soft photograph of ripples on calm water" style="left:90px;top:0;width:156px;height:154px"></div>
  <div class="brand" style="left:18px;top:20px;font-size:7.5px"><span class="mark"></span><span>Marlow<br>Advisory</span></div>
  <div class="abs headline">Your Presentation Title</div>
  <div class="abs tagline">Your Best Tagline Goes Here</div>
  <div class="abs byline"><b>By Daniel Marlow</b>, PhD<br>Professor<br>Organisational Culture &amp; Leadership</div>
</section>

<!-- Presentation: biography slide -->
<section class="piece slide slide-bio" style="left:372px;top:115px;background:#f4f6f8">
  <div class="abs band"></div>
  <div class="abs portrait" role="img" aria-label="Portrait photograph of the founder in a navy suit outdoors"></div>
  <div class="brand" style="right:8px;top:5px;font-size:3px"><span class="mark"></span><span>Marlow<br>Advisory</span></div>
  <div class="abs copy">
    <h3>Authentic. Empathic. Purposeful.<br>Trusted.</h3>
    <div class="role">Daniel Marlow – Professor of Organisational Culture and Leadership</div>
    <div class="rule"></div>
    <p>Daniel is a specialist in the deep cultural change that professionals need in their workplace. Such culture operates at the crucial experiential level – that of the informal organisation.</p>
    <p>He helps leading private, public and government organisations catalyse effective cultural change. As professor at leading universities in the UK and Australia, he has a specialist focus in executive education. He is an accredited individual and group psychotherapist, and an executive coach.</p>
    <p>Before his business-school career, he was a public health clinical director and lead consultant psychotherapist, working in major teaching hospitals. He holds a PhD in organisational culture and leadership.</p>
  </div>
</section>

<!-- Presentation: services slide -->
<section class="piece slide slide-services" style="left:101px;top:285px;background:#f3f5f8">
  <div class="brand" style="right:8px;top:6px;font-size:3px"><span class="mark"></span><span>Marlow<br>Advisory</span></div>
  <div class="abs dash"></div>
  <div class="abs intro">At Marlow Advisory, we catalyse the deep cultural change needed<br>to create humane, people-centred workplaces.</div>
  <div class="service" style="left:20px"><span class="corner"></span>
    <svg width="26" height="26" viewBox="0 0 26 26" fill="none" stroke="#0054AA" stroke-width="1"><circle cx="13" cy="13" r="11"/><path d="M8 17l4-4M15 9l3 3M18 9l-3 3M8 9l3 3M11 9l-3 3"/></svg>
    <b>Craft sustainable strategies</b> that harness personal motivations, energies and resources.</div>
  <div class="service" style="left:91px"><span class="corner"></span>
    <svg width="26" height="26" viewBox="0 0 26 26" fill="none" stroke="#0054AA" stroke-width="1"><circle cx="13" cy="4" r="2"/><circle cx="4" cy="13" r="2"/><circle cx="22" cy="13" r="2"/><circle cx="13" cy="22" r="2"/><circle cx="13" cy="13" r="6"/></svg>
    <b>Build highly effective teams</b> that generate psychological safety and better performance.</div>
  <div class="service" style="left:162px"><span class="corner"></span>
    <svg width="26" height="26" viewBox="0 0 26 26" fill="none" stroke="#0054AA" stroke-width="1"><circle cx="13" cy="13" r="11"/><circle cx="13" cy="13" r="8"/><path d="M10 16l2-5 4-1-2 5z"/></svg>
    <b>Navigate tricky leadership dynamics</b> to create healthier relationships at work.</div>
</section>

<!-- Presentation: closing slide -->
<section class="piece slide slide-thanks" style="left:372px;top:284px">
  <div class="abs scene" role="img" aria-label="Soft white architectural interior photograph"></div>
  <div class="brand" style="left:19px;top:19px;font-size:5.5px"><span class="mark"></span><span>Marlow<br>Advisory</span></div>
  <div class="abs headline">Thank You</div>
  <div class="abs tagline">Your Best Tagline Goes Here</div>
  <div class="abs contact" style="left:19px;top:125px"><i></i>+61 3 9100 2270<br><i></i>info@marlowadvises.com<br><i></i>www.marlowadvises.com</div>
  <div class="abs contact" style="left:68px;top:129px">Suite 12/48 Elm Row<br>Fitzroy, Victoria, Australia</div>
  <div class="abs accr">Accredited by</div>
  <div class="badge" style="left:162px;width:12px;height:12px;border-radius:50%"></div>
  <div class="badge" style="left:180px;width:22px;height:10px;top:125px;background:#d9e2ec"></div>
  <div class="badge" style="left:208px;width:20px;height:10px;top:125px;background:#8a6fb0"></div>
</section>

<!-- Letterhead -->
<section class="piece letterhead">
  <div class="brand" style="left:16px;top:13px;font-size:9px"><span class="mark"></span><span>Marlow<br>Advisory</span></div>
  <div class="abs divider" style="left:137px;top:14px;height:12px"></div>
  <div class="abs contact" style="left:140px;top:14px"><i></i>+61 3 9100 2270<br><i></i>info@marlowadvises.com<br><i></i>www.marlowadvises.com</div>
  <div class="abs body">
    <p>01 January 2050</p>
    <p>Company (Pvt) Ltd.<br>PO Box 3355 Mainville St<br>Sample City Country 3355</p>
    <p>Dear Alan Greaves,</p>
    <p>Thank you for the time you gave us last week. As discussed, our work begins with listening: we meet leaders and teams where they are, map the informal culture that shapes daily behaviour, and agree together on the changes that matter most. This letter outlines the scope, timing and people involved in the first phase of our partnership, and invites your feedback before we finalise the plan.</p>
    <p>The first phase combines interviews, small group sessions and a short survey. We then share findings with your executive team in a facilitated workshop, and shape a practical roadmap that builds trust, psychological safety and clear accountability across the organisation.</p>
    <p>We look forward to working with you and your colleagues. Please let us know if any details need adjusting, or if you would like to arrange a call to discuss the proposal further before the next board meeting.</p>
    <p style="margin-top:10px">Sincerely Yours</p>
    <div class="signature">Henry Aldous</div>
  </div>
  <div class="abs contact" style="left:16px;top:270px">Suite 12/48 Elm Row, Fitzroy, Victoria, Australia</div>
</section>

<!-- Business card front -->
<section class="piece card" style="left:869px;top:154px">
  <div class="brand" style="left:7px;top:21px;font-size:5px"><span class="mark"></span><span>Marlow<br>Advisory</span></div>
  <div class="abs divider" style="left:45px;top:17px;height:20px"></div>
  <div class="abs" style="left:50px;top:18px;font-family:var(--serif);font-size:2.8px;color:var(--brand)">DANIEL MARLOW, PhD</div>
  <div class="abs contact" style="left:50px;top:21px;font-size:1.9px">Founder<br><i></i>+61 3 9100 2270<br><i></i>info@marlowadvises.com<br><i></i>www.marlowadvises.com</div>
  <div class="abs contact" style="left:20px;top:44px;font-size:1.8px">Suite 12/48 Elm Row, Fitzroy, Victoria, Australia</div>
</section>

<!-- Business card back -->
<section class="piece card card-back" style="left:869px;top:223px">
  <div class="abs strap">TRANSFORMING CULTURES<span>One leader, one team, one organisation at a time.</span></div>
</section>

<!-- Email footer -->
<section class="piece email">
  <div class="abs avatar" role="img" aria-label="Small round portrait of the founder"></div>
  <div class="dot" style="left:12px"></div><div class="dot" style="left:18px"></div><div class="dot" style="left:24px"></div><div class="dot" style="left:30px"></div><div class="dot" style="left:36px"></div>
  <div class="abs" style="left:54px;top:10px;font-family:var(--serif);font-size:5.2px;color:var(--brand)">DANIEL MARLOW, PhD</div>
  <div class="abs" style="left:54px;top:16px;font-size:3.6px">Founder</div>
  <div class="abs contact" style="left:54px;top:23px;font-size:3.4px"><i></i>+61 3 9100 2270<br><i></i>info@marlowadvises.com<br><i></i>www.marlowadvises.com</div>
  <div class="abs contact" style="left:54px;top:41px;font-size:3.4px">Suite 12/48 Elm Row, Fitzroy, Victoria, Australia</div>
  <div class="brand" style="left:128px;top:9px;font-size:6.5px"><span class="mark"></span><span>Marlow<br>Advisory</span></div>
  <div class="abs rule-bottom"></div>
</section>

<!-- Envelope front -->
<section class="piece envelope env-front">
  <div class="brand" style="left:14px;top:14px;font-size:8px"><span class="mark"></span><span>Marlow<br>Advisory</span></div>
  <div class="abs contact" style="left:14px;top:72px"><i></i>+61 3 9100 2270<br><i></i>info@marlowadvises.com<br><i></i>www.marlowadvises.com</div>
  <div class="abs contact" style="left:63px;top:76px">Suite 12/48 Elm Row<br>Fitzroy, Victoria, Australia</div>
</section>

<!-- Envelope back -->
<section class="piece envelope env-back">
  <svg class="abs" style="left:0;top:0" width="219" height="34" viewBox="0 0 219 34"><path d="M0 0H219L212 30Q211 33 207 33H12Q8 33 7 30Z" fill="#0054AA"/></svg>
  <div class="abs" style="left:104px;top:12px;width:8px;height:8px;background:#fff"></div>
</section>

<!-- Proposal cover spread -->
<section class="piece proposal">
  <div class="abs back" role="img" aria-label="Solid brand blue back cover with subtle tonal pattern"></div>
  <div class="brand on-blue" style="left:22px;top:250px;font-size:6.5px"><span class="mark"></span><span>Marlow<br>Advisory</span></div>
  <div class="abs contact light" style="left:137px;top:248px"><i></i>Suite 12/48 Elm Row<br>&nbsp;&nbsp;&nbsp;Fitzroy, Victoria, Australia<br><i></i>+61 3 9100 2270<br><i></i>info@marlowadvises.com<br><i></i>www.marlowadvises.com</div>
  <div class="abs water" role="img" aria-label="Photograph of ripples spreading on calm blue water"></div>
  <div class="brand" style="left:223px;top:20px;font-size:9px"><span class="mark"></span><span>Marlow<br>Advisory</span></div>
  <div class="abs kicker">BUSINESS PROJECT</div>
  <div class="abs title">PROPOSAL</div>
  <div class="abs date">ISSUED DATE: 01 FEB 2022</div>
  <div class="abs" style="left:223px;top:164px;width:19px;height:1.5px;background:var(--brand)"></div>
</section>

<!-- Project folder (flat) -->
<section class="piece folder">
  <div class="abs inner">
    <div class="brand on-blue" style="left:20px;top:238px;font-size:6.5px"><span class="mark"></span><span>Marlow<br>Advisory</span></div>
    <div class="abs contact light" style="left:112px;top:232px"><i></i>Suite 12/48 Elm Row, Fitzroy<br><i></i>+61 3 9100 2270<br><i></i>info@marlowadvises.com<br><i></i>www.marlowadvises.com</div>
  </div>
  <div class="abs cover">
    <svg class="abs" style="left:0;top:0" width="190" height="270" viewBox="0 0 190 270"><polygon points="0,55 190,120 190,270 0,270" fill="#0054AA"/><polygon points="0,55 190,120 190,160 0,110" fill="#0677BA" opacity=".55"/></svg>
    <div class="abs ripple" role="img" aria-label="Faint photograph of ripples on deep blue water" style="left:90px;top:170px;width:100px;height:60px;opacity:.15"></div>
    <div class="brand" style="right:14px;top:18px;font-size:8px"><span class="mark"></span><span>Marlow<br>Advisory</span></div>
    <div class="abs strap">TRANSFORMING CULTURES<span>One leader, one team, one organisation at a time.</span></div>
  </div>
</section>

</body>
</html>
```